Splash Page Design For Thailands "Whatever Suits Me" App

We are creating an app that will allow a tourist to request a variety of services on demand. Such as motorbike rentals, in room massage, pick up and laundry delivery service, maid cleaning service, etc.

We want to design a splash page that tourists will initially go to when they want to choose a service that we offer.

INSTRUCTIONS:
This page must speak to tourists in Phuket, Thailand. Should be Thailand Island theme.

GO 4 IT (logo)

CONTENT:

ALL YOU NEED WHILE TRAVELING IN PHUKET, THAILAND

CHOOSE A SERVICE BELOW TO GET STARTED

MOTORBIKE RENTALS
ACTIVITY AND TOUR PACKAGES (COMING SOON)
LAUNDRY PICK UP AND DELIVER SERVICE (COMING SOON)
MAID SERVICE (COMING SOON)
MASSAGE SERVICE TO YOUR ROOM (COMING SOON)
VISA SERVICE (COMING SOON)

Target Market(s)

TOURISTS IN PHUKET THAILAND

Industry/Entity Type

TOURISM

Number of Pages Required

1 page

Requirements
Must have
• We are creating an app that will allow a tourist to request a variety of services on demand. Such as motorbike rentals, in room massage, pick up and laundry delivery service, maid cleaning service, etc. We want to design a splash page that tourists will initially go to when they want to choose a service that we offer. INSTRUCTIONS: This page must speak to tourists in Phuket, Thailand. Should be Thailand Island theme. GO 4 IT (logo) CONTENT: ALL YOU NEED WHILE TRAVELING IN PHUKET, THAILAND CHOOSE A SERVICE BELOW TO GET STARTED MOTORBIKE RENTALS ACTIVITY AND TOUR PACKAGES (COMING SOON) LAUNDRY PICK UP AND DELIVER SERVICE (COMING SOON) MAID SERVICE (COMING SOON) MASSAGE SERVICE TO YOUR ROOM (COMING SOON) VISA SERVICE (COMING SOON)
Nice to have
Should not have

```html
<!DOCTYPE html>
<html lang="en">
<head>
<meta charset="utf-8">
<title>Go 4 It – Whatever Suits Me While In Phuket</title>
<link rel="stylesheet" href="https://fonts.googleapis.com/css2?family=Roboto:wght@400;500;700;900&family=Lato:wght@400&display=swap">
<style>
:root{
  --orange:#f47a10;
  --ink:#1e1e1e;
  --muted:#666;
  --cream:#fbf2e8;
  --white:#ffffff;
  --band:rgba(25,25,25,.78);
  --black:#0c0c0c;
}
*{box-sizing:border-box;margin:0;padding:0}
html,body{width:1200px;height:2752px;overflow:hidden}
body{position:relative;background:var(--cream);font-family:'Roboto',Arial,sans-serif;color:var(--ink)}
.hero-art{position:absolute;left:0;top:0;width:1200px;height:900px;
  background:
    linear-gradient(180deg,rgba(251,242,232,0) 78%,var(--cream) 100%),
    linear-gradient(180deg,#2f72d8 0%,#5d9ee6 28%,#9fc7ee 45%,#3f8a3a 52%,#2aa7a8 70%,#52d1c1 77%,#ecdcc6 86%,#f6ead9 100%)}
.header{position:absolute;left:0;top:0;width:1200px;height:120px}
.brand{position:absolute;left:111px;top:22px}
.brand-name{font-weight:900;font-size:66px;line-height:1;color:var(--orange);letter-spacing:1px;white-space:nowrap}
.brand-tag{font-weight:500;font-size:11px;letter-spacing:1px;color:var(--orange);margin-top:10px;text-transform:uppercase;white-space:nowrap}
.topbar{position:absolute;right:253px;top:22px;display:flex;align-items:center;gap:10px;color:var(--white);font-weight:500;font-size:18px;white-space:nowrap}
.topbar svg{width:16px;height:16px;fill:var(--orange);margin-right:6px;vertical-align:-2px}
.login{position:absolute;left:965px;top:9px;width:123px;height:51px;border-radius:26px;background:var(--orange);color:var(--white);font-weight:500;font-size:18px;display:flex;align-items:center;justify-content:center;gap:6px}
.login svg{width:12px;height:14px;fill:var(--white)}
.nav{position:absolute;right:111px;top:78px;display:flex;gap:28px;font-weight:500;font-size:16px;color:var(--white);white-space:nowrap}
.nav .active{color:var(--orange)}
.hero-text{position:absolute;left:0;top:352px;width:1200px;text-align:center;color:var(--white)}
.hero-text .lead{font-size:52px;font-weight:400;line-height:1}
.hero-text .main{font-size:98px;font-weight:900;line-height:1;margin-top:20px;letter-spacing:1px}
.services-title{position:absolute;left:0;top:905px;width:1200px;text-align:center;font-weight:700;font-size:45px;line-height:52px;color:var(--ink)}
.card{position:absolute;width:316px}
.card-photo{position:relative;height:300px;border-radius:48px 0 48px 0;overflow:hidden}
.soon{position:absolute;left:0;top:201px;width:100%;height:56px;background:var(--band);color:var(--white);font-weight:700;font-size:22px;display:flex;align-items:center;justify-content:center}
.card-title{margin-top:20px;text-align:center;font-weight:500;font-size:24px;line-height:29px;color:var(--ink)}
.c1{left:111px;top:1058px}.c2{left:442px;top:1058px}.c3{left:773px;top:1058px}
.c4{left:111px;top:1471px}.c5{left:442px;top:1471px}.c6{left:773px;top:1471px}
.p-bike{background:linear-gradient(160deg,#d7b07a,#b9a690 55%,#8d8b86)}
.p-tour{background:linear-gradient(160deg,#6fa8d8,#d08a46 45%,#3b5f8a)}
.p-laundry{background:linear-gradient(160deg,#3a3a3a,#e7e3de 50%,#bdb8b3)}
.p-maid{background:linear-gradient(160deg,#1b1b1b 20%,#f2f2f2 45%,#bfe0ec)}
.p-massage{background:linear-gradient(160deg,#2a1e18,#c58b6e 45%,#e0b37a)}
.p-visa{background:linear-gradient(160deg,#3b3b3b,#d9ccc2 50%,#505a63)}
.cta{position:absolute;left:511px;top:1914px;width:177px;height:60px;border-radius:30px;background:var(--orange);color:var(--white);font-weight:500;font-size:19px;display:flex;align-items:center;justify-content:center}
.boats-art{position:absolute;left:0;top:1998px;width:1200px;height:321px;
  background:
    linear-gradient(180deg,var(--cream) 0%,rgba(251,242,232,0) 22%,rgba(251,242,232,0) 75%,var(--cream) 100%),
    linear-gradient(180deg,#cde8f2 10%,#3f9c8a 30%,#47d0c0 50%,#8fe4d4 75%,#f4efe3 100%)}
.footer-brand{position:absolute;left:111px;top:2382px}
.footer-about{position:absolute;left:111px;top:2518px;width:350px;font-family:'Lato',Arial,sans-serif;font-size:16px;line-height:25px;color:var(--muted)}
.footer-col{position:absolute;top:2378px;font-family:'Lato',Arial,sans-serif;color:var(--muted);font-size:16px;line-height:26.7px}
.footer-col h3{font-family:'Roboto',Arial,sans-serif;font-weight:500;font-size:19px;color:var(--ink);margin-bottom:18px}
.links{left:539px}
.contact{left:759px;width:340px}
.contact .row{display:flex;gap:8px;align-items:flex-start}
.contact svg{width:13px;height:13px;fill:var(--orange);flex:none;margin-top:7px}
.contact .gap{margin-top:26px}
.bottom{position:absolute;left:0;top:2653px;width:1200px;height:99px;background:var(--black);color:var(--white)}
.copy{position:absolute;left:111px;top:38px;font-family:'Lato',Arial,sans-serif;font-size:17px}
.social{position:absolute;right:112px;top:28px;display:flex;gap:9px}
.social span{width:43px;height:43px;border-radius:50%;border:1.5px solid var(--orange)}
</style>
</head>
<body>
<div class="hero-art" role="img" aria-label="Phuket island beach with limestone cliffs, turquoise sea and a longtail boat"></div>

<header class="header">
  <div class="brand">
    <div class="brand-name">GO 4 IT</div>
    <div class="brand-tag">Whatever Suits Me While In Phuket</div>
  </div>
  <div class="topbar">
    <span><svg viewBox="0 0 16 16"><path d="M3.5 1l2.5 3-1.4 1.8a9 9 0 0 0 5.6 5.6L12 10l3 2.5-1.6 2.5C7 15 1 9 1 2.6z"/></svg>1 555 010 0199</span>
    <span>|</span>
    <span><svg viewBox="0 0 16 12"><path d="M0 0h16v12H0z"/><path d="M1 1l7 5 7-5" fill="none" stroke="#fff" stroke-width="1.4"/></svg>hello@go4it.example</span>
  </div>
  <div class="login"><svg viewBox="0 0 12 14"><path d="M2 6V4a4 4 0 0 1 8 0v2h1v8H1V6zm2 0h4V4a2 2 0 0 0-4 0z"/></svg>LOGIN</div>
  <nav class="nav">
    <span class="active">HOME</span><span>ABOUT US</span><span>SERVICES</span><span>NEWS &amp; EVENTS</span><span>CONTACT US</span>
  </nav>
</header>

<section class="hero-text">
  <div class="lead">WHATEVER SUITS ME</div>
  <div class="main">WHILE IN PHUKET</div>
</section>

<h2 class="services-title">CHOOSE A SERVICE BELOW<br>TO GET STARTED</h2>

<div class="card c1"><div class="card-photo p-bike" role="img" aria-label="Row of scooters parked along a sunny street"></div><div class="card-title">Motorbike<br>Rentals</div></div>
<div class="card c2"><div class="card-photo p-tour" role="img" aria-label="Tourist couple relaxing on a longtail boat"><div class="soon">COMING SOON</div></div><div class="card-title">Activity And<br>Tour Packages</div></div>
<div class="card c3"><div class="card-photo p-laundry" role="img" aria-label="Courier delivering fresh laundry from a van"><div class="soon">COMING SOON</div></div><div class="card-title">Laundry Pick Up And<br>Deliver Service</div></div>
<div class="card c4"><div class="card-photo p-maid" role="img" aria-label="Housekeeper holding a stack of white towels"><div class="soon">COMING SOON</div></div><div class="card-title">Maid<br>Service</div></div>
<div class="card c5"><div class="card-photo p-massage" role="img" aria-label="Relaxing facial massage in a hotel room"><div class="soon">COMING SOON</div></div><div class="card-title">Massage Service<br>To Your Room</div></div>
<div class="card c6"><div class="card-photo p-visa" role="img" aria-label="Agent handing over a passport at a visa desk"><div class="soon">COMING SOON</div></div><div class="card-title">Visa<br>Service</div></div>

<div class="cta">GET STARTED</div>

<div class="boats-art" role="img" aria-label="Longtail boats moored in clear turquoise water near small islands"></div>

<footer>
  <div class="footer-brand">
    <div class="brand-name">GO 4 IT</div>
    <div class="brand-tag">Whatever Suits Me While In Phuket</div>
  </div>
  <p class="footer-about">Lorem ipsum dolor sit amet, consectetur adipis cing elit, sed do eiusmod tempor incididunt ut labore et dolore magna aliqua. Ut enim ad mini m veniam, quis nostrud.</p>
  <div class="footer-col links">
    <h3>Quick Links</h3>
    <div>Home</div><div>About Us</div><div>Services</div><div>News &amp; Events</div><div>Contact Us</div>
  </div>
  <div class="footer-col contact">
    <h3>Contact Us</h3>
    <div>Go 4 It</div>
    <div class="row"><svg viewBox="0 0 13 13"><path d="M6.5 0A4.5 4.5 0 0 0 2 4.5C2 8 6.5 13 6.5 13S11 8 11 4.5A4.5 4.5 0 0 0 6.5 0zm0 6.3a1.8 1.8 0 1 1 0-3.6 1.8 1.8 0 0 1 0 3.6z"/></svg><span>No – 45/210, 8th Floor, Harbour House,<br>Patong Beach Road</span></div>
    <div class="row gap"><svg viewBox="0 0 16 16"><path d="M3.5 1l2.5 3-1.4 1.8a9 9 0 0 0 5.6 5.6L12 10l3 2.5-1.6 2.5C7 15 1 9 1 2.6z"/></svg><span>1 555 010 0199</span></div>
    <div class="row gap"><svg viewBox="0 0 16 12"><path d="M0 0h16v12H0z"/><path d="M1 1l7 5 7-5" fill="none" stroke="#fbf2e8" stroke-width="1.4"/></svg><span>hello@go4it.example</span></div>
  </div>
  <div class="bottom">
    <div class="copy">© 2021, Go 4 It. All Rights Reserved.</div>
    <div class="social"><span></span><span></span><span></span></div>
  </div>
</footer>
</body>
</html>
```